Vosky - Business Card Design

Design a modern masculine business card for our business

Target Market(s)

Private Market

Industry/Entity Type

Construction

Contact Information for Business Card

Company Name - Name of Person - Address - email address - contact number

Font styles to use
Serif
Sans Serif

Colors
0094D4
00A9DD
6FCCEA
C7EBF8
E9F6FB
00AB8E
00BBA5
67D7C9
C6EFE9
E9F9F6
F0912C
F2A743
F7CA91
FBE8D2
FDF5EE

Requirements
Must have
• Use company logo provided
Nice to have
• Company Logo

```html
<!DOCTYPE html>
<html lang="en">
<head>
<meta charset="utf-8">
<title>Vosky - Business Card Design</title>
<link rel="stylesheet" href="https://fonts.googleapis.com/css2?family=Montserrat:wght@400;500;700;800&display=swap">
<style>
  :root {
    --ink: #121212;
    --orange: #f0722a;
    --paper: #ffffff;
    --backdrop: #d9d9d9;
    --muted: #2a2a2a;
  }
  * { margin: 0; padding: 0; box-sizing: border-box; }
  html, body {
    width: 1200px; height: 900px; overflow: hidden;
    background: var(--backdrop);
    font-family: "Montserrat", sans-serif;
    color: var(--ink);
  }
  .stage { position: relative; width: 1200px; height: 900px; }
  .card {
    position: absolute; left: 320px; width: 560px; height: 320px;
    background: var(--paper);
    box-shadow: 0 6px 18px rgba(0,0,0,0.25);
    overflow: hidden;
  }
  .card--front { top: 70px; }
  .card--back { top: 470px; }

  .brand { display: flex; align-items: center; gap: 12px; white-space: nowrap; }
  .brand__square { width: 16px; height: 16px; background: var(--orange); flex: none; }
  .brand__name { font-weight: 800; color: var(--ink); text-transform: uppercase; letter-spacing: 1px; line-height: 1; }

  .card--front .brand {
    position: absolute; inset: 0; justify-content: center;
  }
  .card--front .brand__name { font-size: 28px; }
  .card--front .brand__square { width: 22px; height: 22px; }

  .card--back .brand { position: absolute; top: 48px; right: 40px; }
  .card--back .brand__name { font-size: 18px; }

  .person { position: absolute; left: 0; top: 108px; display: flex; align-items: stretch; }
  .person__bar { width: 22px; background: var(--orange); margin-right: 26px; }
  .person__name { font-size: 22px; font-weight: 800; letter-spacing: 0.5px; line-height: 1.1; }
  .person__first { color: var(--orange); }
  .person__title { font-size: 14px; font-weight: 500; margin-top: 4px; color: var(--muted); }

  .address {
    position: absolute; right: 40px; top: 126px; text-align: right;
    font-size: 13px; font-weight: 500; line-height: 1.45; color: var(--muted);
  }

  .contacts { position: absolute; left: 108px; top: 182px; list-style: none; }
  .contacts li { display: flex; align-items: center; gap: 10px; font-size: 13px; font-weight: 500; line-height: 21px; color: var(--muted); }
  .contacts svg { width: 13px; height: 13px; flex: none; }

  .wave { position: absolute; left: 0; top: 0; width: 560px; height: 320px; }
</style>
</head>
<body>
<main class="stage">
  <section class="card card--front" aria-label="Card front">
    <div class="brand">
      <span class="brand__square"></span>
      <span class="brand__name">Vosky Construction, Inc</span>
    </div>
  </section>

  <section class="card card--back" aria-label="Card back">
    <svg class="wave" viewBox="0 0 560 320" preserveAspectRatio="none" aria-hidden="true">
      <path d="M0,272 C150,302 330,252 560,184 L560,320 L0,320 Z" fill="var(--ink)"/>
      <path d="M0,294 C160,320 340,270 560,200 L560,320 L0,320 Z" fill="var(--paper)"/>
      <path d="M0,300 C160,326 340,276 560,206 L560,320 L0,320 Z" fill="var(--orange)"/>
    </svg>

    <div class="brand">
      <span class="brand__square"></span>
      <span class="brand__name">Vosky Construction, Inc</span>
    </div>

    <div class="person">
      <span class="person__bar"></span>
      <div>
        <h1 class="person__name"><span class="person__first">MARTIN</span> KELLER</h1>
        <p class="person__title">Managing Director</p>
      </div>
    </div>

    <p class="address">42-07 Linden St 14<br>Maplewood, NY 11210</p>

    <ul class="contacts">
      <li>
        <svg viewBox="0 0 16 16" aria-hidden="true"><path d="M2 5c0-2 2-3 6-3s6 1 6 3l-3 1-1-1.5H6L5 6 2 5zM4 8h8l1 6H3z" fill="var(--orange)"/></svg>
        555.210.4477
      </li>
      <li>
        <svg viewBox="0 0 16 16" aria-hidden="true"><rect x="1" y="3" width="14" height="10" fill="var(--orange)"/><path d="M1 3l7 6 7-6" stroke="#fff" stroke-width="1.4" fill="none"/></svg>
        info@vosky-mail.com
      </li>
      <li>
        <svg viewBox="0 0 16 16" aria-hidden="true"><circle cx="8" cy="8" r="7" fill="var(--orange)"/><path d="M1 8h14M8 1c-3 3-3 11 0 14M8 1c3 3 3 11 0 14" stroke="#fff" stroke-width="1" fill="none"/></svg>
        www.vosky-web.com
      </li>
    </ul>
  </section>
</main>
</body>
</html>
```